Flyer promoting Velmora's workshops and credentials

We run Training workshops for the data analyst community. We'd like a flyer to sell our services using a style and colour scheme consistent with our website www.velmoraskills.co.uk . I've attached some background info and some existing e-brochures for different workshops to give a flavour for content (but these are poorly designed and we don't want a similar design!!). There's also an overview document which gives more direction. The flyer will be sent with an accompanying letter to Learning & Development decision makers as well as Anlaytical team managers. It's purpose would be to generate enquiries and bookings for primarliy our flagship workshop 'Turning Figures Into Real Results'.

Target Market(s)

Learning and Development senior managers
Analytical team managers

Industry/Entity Type

Training

Font styles to use
Other font styles liked:
• Similar to website for consistency

Requirements
Must have
• Good copy! Slick design more in line with European (UK) style advertising rather than US.
Nice to have
• Some humour,
Should not have
• should not be as boring and non-sales based as the website!! Website is not a great example!

```html
<!DOCTYPE html>
<html lang="en">
<head>
<meta charset="utf-8">
<title>Velmora – Workshops for Data Analysts flyer</title>
<link rel="stylesheet" href="https://fonts.googleapis.com/css2?family=Lato:ital,wght@0,300;0,400;0,700;0,900;1,400&display=swap">
<style>
  :root {
    --orange: #f28a22;
    --orange-deep: #e5761a;
    --navy: #2b3a86;
    --blue: #2f4b9f;
    --blue-mid: #4656a6;
    --ink: #2a2f45;
    --grey: #6b6f7a;
    --line: #b9bcc4;
    --paper: #ffffff;
    --stage: #e4e5e8;
  }
  * { box-sizing: border-box; margin: 0; padding: 0; }
  html, body { width: 1200px; height: 1200px; overflow: hidden; }
  body { background: var(--stage); font-family: "Lato", Arial, sans-serif; color: var(--ink); position: relative; }

  .page { position: absolute; top: 218px; width: 540px; height: 764px; background: var(--paper); overflow: hidden; box-shadow: 0 8px 24px rgba(0,0,0,.18); }
  .page--front { left: 40px; }
  .page--back { left: 620px; }
  .abs { position: absolute; }

  /* brand */
  .brand { display: flex; flex-direction: column; }
  .brand__name { font-weight: 700; font-size: 36px; line-height: 1; color: var(--navy); display: flex; align-items: center; gap: 7px; }
  .brand__dot { width: 12px; height: 12px; border-radius: 50%; background: var(--orange); }
  .brand__tag { font-size: 10.5px; font-weight: 700; color: var(--orange); margin-left: 36px; margin-top: 2px; }

  /* front */
  .hero-photo { left: 190px; top: 0; width: 350px; height: 240px; background: linear-gradient(100deg, #ffffff 0%, #eef0f4 30%, #d7dbe3 70%, #c9ced8 100%); }
  .front-shapes { left: 0; top: 0; }
  .headline { left: 22px; top: 138px; width: 340px; color: #fff; font-weight: 700; font-size: 22px; line-height: 1.02; }

  .testimonials { left: 10px; top: 234px; width: 254px; height: 168px; background: #fff; border: 2px solid var(--line); box-shadow: 0 2px 4px rgba(0,0,0,.15); padding: 10px 14px; }
  .testimonials__title { font-size: 18px; font-weight: 400; color: var(--navy); margin-bottom: 8px; }
  .quote { font-style: italic; font-size: 9.5px; color: var(--grey); line-height: 1.3; }
  .quote__by { display: block; text-align: right; font-style: normal; font-size: 13.5px; color: var(--navy); margin-top: 2px; }
  .quote + .quote { margin-top: 12px; }

  .brief-column { left: 278px; top: 244px; width: 254px; font-size: 6.6px; line-height: 1.28; }
  .brief-column__intro { color: #fff; padding: 0 4px; }
  .about-tab { margin: 8px -14px 6px -10px; background: var(--blue); color: #fff; padding: 4px 10px; }
  .about-tab__label { font-size: 15px; font-weight: 400; line-height: 1.05; }
  .about-tab__title { font-size: 11px; font-weight: 700; }
  .brief-column__about { color: #fff; padding: 0 4px; }
  .issues { color: var(--navy); font-size: 7.6px; line-height: 1.2; padding: 5px 4px 0 18px; font-weight: 400; }
  .issues li { margin-bottom: 2px; }

  .section-heading { font-weight: 700; font-size: 20px; color: var(--orange); text-transform: uppercase; letter-spacing: .2px; }
  .prev-marketing { left: 16px; top: 416px; width: 256px; }
  .prev-marketing p { font-size: 7.2px; color: var(--grey); line-height: 1.3; margin-top: 6px; }

  .workshops-band { left: 0; top: 498px; }
  .workshops-title { left: 20px; top: 503px; color: #fff; font-size: 19px; font-weight: 400; text-transform: uppercase; }
  .workshops-photo { left: 12px; top: 546px; width: 148px; height: 74px; background: linear-gradient(135deg, #e9ecf3, #b9c3d9 60%, #8fa0c4); }
  .workshops-copy { left: 166px; top: 548px; width: 106px; font-size: 6.6px; color: var(--grey); line-height: 1.3; }

  .front-footer { left: 0; top: 626px; width: 540px; height: 138px; background: var(--blue); color: #fff; }
  .audience { left: 20px; top: 20px; width: 238px; }
  .audience h3 { font-size: 15px; font-weight: 700; }
  .audience p { font-size: 10.5px; line-height: 1.25; }
  .audience ol { list-style: none; font-size: 10.5px; font-weight: 700; margin-top: 6px; line-height: 1.3; }
  .office { font-size: 8.5px; line-height: 1.25; }
  .office strong { font-size: 11px; display: block; }
  .front-footer .office { left: 276px; top: 20px; }
  .contact { font-size: 14px; }
  .contact b { font-weight: 700; }
  .contact small { display: block; font-size: 10.5px; margin-top: 6px; }
  .front-footer .contact { left: 370px; top: 28px; }

  /* back */
  .team-photo { left: 0; top: 0; }
  .softskills-heading { left: 18px; top: 334px; width: 200px; text-align: right; font-size: 18px; font-weight: 700; color: var(--ink); line-height: 1.3; }
  .softskills-copy { left: 246px; top: 288px; width: 276px; font-size: 7.6px; color: var(--grey); line-height: 1.3; }
  .ladder { left: 0; top: 0; }
  .ladder text { font-family: "Lato", Arial, sans-serif; font-weight: 700; font-size: 7.6px; }
  .ladder .step-label { fill: #fff; }
  .ladder .role-label { fill: var(--navy); }
  .trainer-photo { left: 256px; top: 420px; width: 284px; height: 196px; background: linear-gradient(160deg, #ffffff 0%, #eef0f5 35%, #cfd5e2 70%, #a9b3c9 100%); }
  .back-footer { left: 0; top: 610px; width: 540px; height: 154px; background: linear-gradient(100deg, #f6a95c 0%, var(--orange) 45%, var(--orange-deep) 100%); color: #fff; }
  .back-footer .brand { left: 20px; top: 62px; }
  .back-footer .brand__name { color: #fff; font-size: 30px; }
  .back-footer .brand__dot { background: #fff; }
  .back-footer .brand__tag { color: #fff; font-weight: 400; margin-left: 30px; }
  .back-footer .office { right: 20px; top: 14px; text-align: right; font-size: 10px; }
  .back-footer .office strong { font-size: 12px; }
  .back-footer .contact { right: 20px; top: 104px; text-align: right; font-size: 15px; }
  .back-footer .contact small { font-size: 12px; font-weight: 700; margin-top: 2px; }
</style>
</head>
<body>

<!-- Front page -->
<section class="page page--front">
  <div class="abs hero-photo" role="img" aria-label="Photo of a hand holding a pen over printed charts"></div>

  <svg class="abs front-shapes" width="540" height="764" viewBox="0 0 540 764" aria-hidden="true">
    <rect x="0" y="130" width="372" height="92" fill="var(--orange)"/>
    <polygon points="372,222 540,196 540,244 278,244 300,222" fill="var(--orange)"/>
    <polygon points="300,222 372,222 300,236" fill="#3a3a3a"/>
    <rect x="278" y="244" width="262" height="382" fill="var(--orange)"/>
  </svg>

  <div class="abs brand" style="left:24px;top:36px;">
    <span class="brand__name"><span class="brand__dot"></span>Velmora</span>
    <span class="brand__tag">Workshops for Data Analysts</span>
  </div>

  <h1 class="abs headline">We help your data analysts to have a real impact on your organisation</h1>

  <aside class="abs testimonials">
    <h2 class="testimonials__title">Testimonials</h2>
    <p class="quote">“A very useful course with a very engaging trainer. Excellent examples that related to our work.” <span class="quote__by">— Delegate, Northline Rail</span></p>
    <p class="quote">“Excellent introduction to the key statistical techniques used in direct marketing.” <span class="quote__by">— Dan Priestley, Harlow Insurance</span></p>
  </aside>

  <div class="abs brief-column">
    <p class="brief-column__intro">What I want ideally is for companies to take the ‘Turning Figures Into Real Results’ workshop (2 days for up to 8 analysts) and privately host it rather than necessarily just have them attend the public workshops. With some companies the workshop has become part of their standard programme of training for analysts so every 12-18-24 months they come back to me and say we’ve now got a bunch of new analysts we want to put through the workshop and that’s ideally what I want to happen in the long term.</p>
    <div class="about-tab">
      <div class="about-tab__label">About</div>
      <div class="about-tab__title">‘Turning Figures Into Real Results’</div>
    </div>
    <p class="brief-column__about">This is my flagship 2 day workshop – if I get to speak to Analytical managers it’s usually a reasonably easy sell – it gives the analysts a number of practical steps and expected behaviours they can follow to ensure they deliver good analytical service whilst also improving their impact and increasing productivity by reducing re-work. Ultimately for any level of analyst it provides a template of standards to work to that will naturally help build credibility and trust with customers and enable them to work more proactively. At the end of the workshop they get a checklist of behaviours and actions as an aide memoire – a few businesses have gone on to integrate this into their personal development review processes. There are a number of common issues/challenges analytical teams face and experience. These are –</p>
    <ol class="issues">
      <li>They have (or rather take on) too much work (usually because they don’t plan effectively or they avoid negotiating deadlines and say yes to everything).</li>
      <li>They work reactively and find no time to add value.</li>
      <li>Their customers don’t involve them in the wider process and so they don’t feel they get the full picture and don’t get involved until last minute.</li>
      <li>They feel their customers don’t articulate themselves very well and are prone to changing their minds so they do lots of re-work.</li>
      <li>Their customers think that everything is just a press of a button whilst in reality it’s a lot more work than that.</li>
      <li>They struggle to get heard and suffer from a low profile within the business.</li>
      <li>They feel as though they spend a lot of time just turning the cog to spew out data.</li>
    </ol>
  </div>

  <div class="abs prev-marketing">
    <h2 class="section-heading">Previous Marketing</h2>
    <p>This year I started to differentiate my marketing into prospects and customers whereas previously I sent everyone the same thing. So customers get updates and offers generally – prospects get a salesy email here are a few and their open/click rates.</p>
  </div>

  <svg class="abs workshops-band" width="280" height="40" viewBox="0 0 280 40" aria-hidden="true">
    <polygon points="0,4 276,0 276,34 0,38" fill="var(--blue)"/>
  </svg>
  <h2 class="abs workshops-title">Workshops &amp; Seminars</h2>
  <div class="abs workshops-photo" role="img" aria-label="Photo of a team working around a table with documents"></div>
  <p class="abs workshops-copy">Velmora’s workshops are interactive and practical. Delegates can attend one of the scheduled public workshops or if you have several analysts, an on-site private workshop offers significant savings and the chance to work through challenges as a team.</p>

  <footer class="abs front-footer">
    <div class="abs audience">
      <h3>Audience</h3>
      <p>There are two main audiences and the message may need to be different for the two –</p>
      <ol>
        <li>a.&nbsp; HR &amp; Training and development people</li>
        <li>b.&nbsp; Analytical team managers</li>
      </ol>
    </div>
    <div class="abs office">
      <strong>Registered Office:</strong>
      4 Birch Yard,<br>Oakdene,<br>Millbrook,<br>Cheshire,<br>SK9 4QT
    </div>
    <div class="abs contact">
      Tel: <b>0161 555 0142</b>
      <small>info@velmoraskills.co.uk</small>
    </div>
  </footer>
</section>

<!-- Back page -->
<section class="page page--back">
  <svg class="abs team-photo" width="540" height="300" viewBox="0 0 540 300" role="img" aria-label="Blue-tinted photo of colleagues reviewing charts and a tablet on a desk">
    <defs>
      <linearGradient id="teamTint" x1="0" y1="0" x2="1" y2="1">
        <stop offset="0" stop-color="#5a64b0"/>
        <stop offset=".5" stop-color="#8d95cc"/>
        <stop offset="1" stop-color="#6e78bd"/>
      </linearGradient>
    </defs>
    <polygon points="0,0 540,0 540,244 0,294" fill="url(#teamTint)"/>
  </svg>

  <h2 class="abs softskills-heading">Soft skills to an analysts development</h2>
  <p class="abs softskills-copy">The workshop addresses all these challenges through sections dedicated to communication, planning and presenting data.<br>I have lots of testimonials for the workshop and it’s now CPD accredited which is another reason why it’s a good lead product. I guess for the two audiences there are two hooks…<br>Training/HR – CPD accredited soft skills training specifically developed for data analysts, data scientists, Management Information and Business Intelligence professionals.<br>Analytical Managers – Complementary soft skills training to help the analysts to become more proactive and customer orientated/consultative.</p>

  <svg class="abs ladder" width="260" height="620" viewBox="0 0 260 620" aria-label="Skills ladder from technician to team leader">
    <polygon points="19,380 19,380 75,445 19,445" fill="var(--navy)"/>
    <polygon points="19,447 77,447 99,473 19,473" fill="var(--blue-mid)"/>
    <polygon points="19,475 101,475 124,502 19,502" fill="var(--navy)"/>
    <polygon points="19,504 126,504 153,535 19,535" fill="var(--blue)"/>
    <polygon points="19,537 155,537 200,590 19,590" fill="var(--blue-mid)"/>
    <text class="step-label" x="26" y="428">LEADER</text>
    <text class="step-label" x="26" y="437">SHIP</text>
    <text class="step-label" x="26" y="459">STRATEGIC</text>
    <text class="step-label" x="26" y="468">THINKING</text>
    <text class="step-label" x="26" y="487">COMMERCIAL</text>
    <text class="step-label" x="26" y="496">AWARENESS</text>
    <text class="step-label" x="26" y="516">INTERPERSONAL SKILLS/</text>
    <text class="step-label" x="26" y="525">OUTWARD THINKING</text>
    <text class="step-label" x="26" y="562">TECHNICAL SKILLS</text>
    <text class="role-label" x="86" y="426">TEAMLEADER/</text>
    <text class="role-label" x="86" y="435">MANAGER</text>
    <text class="role-label" x="106" y="462">CONSULTANT</text>
    <text class="role-label" x="132" y="486">SENIOR</text>
    <text class="role-label" x="132" y="495">ANALYST</text>
    <text class="role-label" x="160" y="520">JUNIOR</text>
    <text class="role-label" x="160" y="529">ANALYST</text>
    <text class="role-label" x="186" y="566">TECHNICIAN</text>
  </svg>

  <div class="abs trainer-photo" role="img" aria-label="Photo of a trainer presenting a bar chart to seated delegates"></div>

  <footer class="abs back-footer" role="img" aria-label="Orange-tinted photo of an office desk behind the contact details">
    <div class="abs brand">
      <span class="brand__name"><span class="brand__dot"></span>Velmora</span>
      <span class="brand__tag">Workshops for Data Analysts</span>
    </div>
    <div class="abs office">
      <strong>Registered Office:</strong>
      4 Birch Yard,<br>Oakdene,<br>Millbrook,<br>Cheshire,<br>SK9 4QT
    </div>
    <div class="abs contact">
      Tel: <b>0161 555 0142</b>
      <small>info@velmoraskills.co.uk</small>
    </div>
  </footer>
</section>

</body>
</html>
```